Flyer for Encounter G.L.O. - Hour of Glory!

We are producing a monthly Hour of Glory that supports local Christian Contemporary artists and raises money for charities. We are looking for a flyer design for our flyers, posters, and postcards (some mailed and some handed out). We want to create a modern and impressive flyer that will capture audiences.

Event details -
Tag: experience the night. praise the night.
A Hour of Glory you will not want to miss
Let's worship! Live band covering your favorite popular contemporary Christian music! All ages welcome!
Date: Wednesday, May 27th, 2015
7:00 pm to 8:15 pm
Location: The Harborview Chapel
2715 W Maple Crest Rd; Fort Lauderdale, FL 33918

Event is FREE!! Please bring a donation of gently used clothing items or new toiletry item.
Benefit for: The Open Hands Mission

This month's debut artist: Talia Verhoeven - local Christian Singer/Songwriter.

for more details, visit: www.encounterpraiseGLO.example
brought to you by: Delphine Marsh Music
___
Please see our website for style of what we are looking for. Also attached is a template design that I like and would love to see if we can do something like this.

Target Market(s)

all ages - young, older, modern, contemporary - youth

Industry/Entity Type

Artists

Colors
ec1f27
6b449b
ffffff

Requirements
Must have
• Cool design, bring a new "vibe" to Christian music -
• Black design
• worship photos like in the attached template ideas.

```html
<!DOCTYPE html>
<html lang="en">
<head>
<meta charset="utf-8">
<title>Encounter G.L.O. - Hour of Glory</title>
<link href="https://fonts.googleapis.com/css2?family=Oswald:wght@400;500;700&family=Anton&family=Montserrat:wght@400;600;700&display=swap" rel="stylesheet">
<style>
  :root{
    --night:#150c2b;
    --deep:#241446;
    --violet:#6b449b;
    --lilac:#a58fd6;
    --red:#ec1f27;
    --white:#ffffff;
    --paper:#f4f2f7;
    --ink:#2a1c44;
  }
  *{margin:0;padding:0;box-sizing:border-box}
  html,body{width:849px;height:1200px;overflow:hidden;background:var(--night)}
  .flyer{
    position:relative;width:849px;height:1200px;overflow:hidden;
    background:linear-gradient(180deg,var(--night) 0%,var(--deep) 45%,#2e1a5a 75%,var(--night) 100%);
    font-family:"Montserrat",sans-serif;color:var(--white);
  }
  .tagline{position:absolute;top:30px;left:58px;right:58px;z-index:2}
  .tagline__main{font-family:"Oswald",sans-serif;font-weight:700;font-size:32px;line-height:1.15;letter-spacing:1px;text-transform:uppercase}
  .tagline__sub{font-family:"Oswald",sans-serif;font-weight:400;font-size:24px;line-height:1.2;margin-top:2px}
  .band-photo{
    position:absolute;top:132px;left:0;width:849px;height:350px;
    background:radial-gradient(ellipse at 50% 35%,#b89be8 0%,#7c56bd 25%,#3f2479 60%,var(--night) 100%);
  }
  .event-mark{
    position:absolute;top:415px;right:48px;display:flex;align-items:center;gap:10px;
    font-family:"Oswald",sans-serif;font-weight:700;font-size:36px;line-height:1;text-transform:uppercase;color:var(--white);
  }
  .event-mark__dot{width:18px;height:18px;border-radius:50%;background:var(--red)}
  .date{position:absolute;top:500px;left:58px;height:210px;width:330px}
  .date__weekday{
    position:absolute;left:0;top:0;width:50px;height:210px;
    writing-mode:vertical-rl;transform:rotate(180deg);text-align:center;
    font-family:"Oswald",sans-serif;font-weight:700;font-size:40px;letter-spacing:2px;text-transform:uppercase;
  }
  .date__month{position:absolute;left:70px;top:-6px;font-family:"Anton",sans-serif;font-size:78px;line-height:1}
  .date__day{position:absolute;left:66px;top:68px;font-family:"Anton",sans-serif;font-size:120px;line-height:1}
  .date__time{position:absolute;left:215px;top:88px;width:120px;font-family:"Oswald",sans-serif;font-weight:700;font-size:26px;line-height:1.1;text-transform:uppercase}
  .divider{position:absolute;top:505px;left:425px;width:3px;height:200px;background:var(--white)}
  .donation{position:absolute;top:500px;left:450px;width:350px}
  .donation__title{font-family:"Oswald",sans-serif;font-weight:700;font-size:50px;line-height:1;text-transform:uppercase}
  .donation__ask{margin-top:12px;width:215px;font-family:"Oswald",sans-serif;font-weight:500;font-size:19px;line-height:1.12;color:var(--red);text-transform:uppercase}
  .charity{position:absolute;top:60px;right:10px;width:120px;text-align:center}
  .charity__shape{width:70px;height:70px;margin:0 auto;border-radius:50%;background:var(--red)}
  .charity__name{margin-top:6px;font-family:"Oswald",sans-serif;font-weight:700;font-size:15px;line-height:1.1;text-transform:uppercase}
  .charity__program{margin-top:14px;font-family:"Oswald",sans-serif;font-weight:500;font-size:18px}
  .venue{position:absolute;top:742px;left:0;right:0;text-align:center;font-family:"Oswald",sans-serif;font-size:22px}
  .venue__name{font-weight:700;text-transform:uppercase;margin-right:8px}
  .artist{position:absolute;top:800px;left:58px;width:340px}
  .artist__label{font-family:"Oswald",sans-serif;font-size:20px}
  .artist-photo{margin-top:8px;width:300px;height:170px;border-radius:4px;
    background:linear-gradient(135deg,#c9a6d9 0%,#8b5fb6 50%,#3f2479 100%)}
  .artist__name{margin-top:10px;font-family:"Oswald",sans-serif;font-weight:700;font-size:30px}
  .artist__role{font-family:"Montserrat",sans-serif;font-size:13px}
  .worship{position:absolute;top:795px;left:450px;width:350px;font-family:"Oswald",sans-serif;text-transform:uppercase}
  .worship__title{font-weight:700;font-size:40px;line-height:1.1}
  .worship__band{margin-top:6px;font-weight:500;font-size:22px;line-height:1.05;color:var(--red)}
  .worship__band strong{display:block;font-size:58px;font-weight:700;line-height:1}
  .worship__ages{margin-top:10px;font-weight:700;font-size:28px}
  .footer{position:absolute;left:0;bottom:0;width:849px;height:92px;background:var(--paper);color:var(--ink);
    display:flex;align-items:center;padding:0 40px;gap:22px;font-family:"Oswald",sans-serif;white-space:nowrap}
  .footer__label{font-size:16px}
  .sponsor{display:flex;align-items:center;gap:8px;font-weight:700;font-size:15px}
  .sponsor__square{width:26px;height:26px;background:var(--ink);flex:none}
  .sponsor__circle{width:26px;height:26px;border-radius:50%;background:var(--violet);flex:none}
  .footer__web{margin-left:auto;font-size:16px;color:var(--violet)}
</style>
</head>
<body>
<main class="flyer">
  <header class="tagline">
    <p class="tagline__main">Experience the night. Praise the night</p>
    <p class="tagline__sub">an hour of glory you will not want to miss</p>
  </header>

  <div class="band-photo" role="img" aria-label="Live worship band performing on stage under purple lights"></div>
  <div class="event-mark"><span class="event-mark__dot"></span>Encounter G.L.O.</div>

  <section class="date">
    <p class="date__weekday">Wednesday</p>
    <p class="date__month">MAY</p>
    <p class="date__day">27</p>
    <p class="date__time">at 7pm until eight fifteen</p>
  </section>

  <div class="divider"></div>

  <section class="donation">
    <p class="donation__title">Free Event!</p>
    <p class="donation__ask">Please bring a donation of a gently used clothing item or new toiletry item. Benefit for:</p>
    <div class="charity">
      <div class="charity__shape"></div>
      <p class="charity__name">The Open Hands Mission</p>
    </div>
    <p class="charity__program">Adult Rehabilitation Program</p>
  </section>

  <p class="venue"><span class="venue__name">The Harborview Chapel</span>2715 W Maple Crest Rd; Fort Lauderdale, FL 33918</p>

  <section class="artist">
    <p class="artist__label">This month's debut artist:</p>
    <div class="artist-photo" role="img" aria-label="Portrait of the debut artist"></div>
    <p class="artist__name">Talia Verhoeven</p>
    <p class="artist__role">local Christian Singer/Songwriter</p>
  </section>

  <section class="worship">
    <p class="worship__title">Let's Worship!</p>
    <p class="worship__band">Live band covering your favorite <strong>Popular</strong>contemporary Christian music!</p>
    <p class="worship__ages">All ages welcome!</p>
  </section>

  <footer class="footer">
    <span class="footer__label">Brought to you by:</span>
    <span class="sponsor"><span class="sponsor__square"></span>Delphine Marsh Music</span>
    <span class="sponsor"><span class="sponsor__circle"></span>The Harborview Chapel</span>
    <span class="footer__web">www.encounterpraiseGLO.example</span>
  </footer>
</main>
</body>
</html>
```